依頼詳細
ウコンのパッケージデザイン(ボトルシール)を依頼させて頂きます。「健康」「お酒にはウコン!!」というイメージをパッケージから感じることができ、ターゲットである居酒屋のお客さんが、何気に注文したくなるデザインを希望します。

・「健康ウコンふりかけ」の“健康”は小さめな字(メインはウコンふりかけ)

・食品表示ありのバージョンもお願いします。
「名称」ウコンふりかけ 「原材料名」秋ウコン(沖縄県産) 「内容量」12g 「賞味期限」 「保存方法」直射日光、高温多湿を避けて保存してください。 「販売者」K&M、沖縄県名護市字北原台4、TEL(FAX)0980-47-2935 その他リサイクル表示やバーコードなど必要なものがあればお願いします。

・希望として色の数はなるべく抑えたいたいです。(経費削減のため)
記載項目
ガラス容器
サイズ:W37mm×H87mm(写真は添付資料参照)
印刷:カラー印刷
紙質:ユポ紙or透明PET
希望イメージ
シンプル 複雑
単色 カラフル
暗い 明るい
日常 高級
遊び心 厳粛
未来的 伝統的
女性的 男性的
希望する色
黄色やゴールド(元気、健康的なイメージ)
納品ファイル
• 高解像度JPG (.jpg)
• イラストレーター形式 (.ai)
• PNG形式 (.png)
補足説明
・添付資料(写真)の容器のキャップは赤になってますが、使用する物は緑となります。

・独立し最初の商品作りでこういった依頼も初めてなので、皆様の多くの依頼をお待ちしております。是非よろしくお願い致します。
「MADE IN OKINAWA」の文字の記載(小さめ)もよろしくお願いします。
・容器の大きさのイメージとしてはよくある唐辛子調味料と同じような大きさです。
すでにすばらしいご提案を頂いておりますが、もう少し多くのご提案を見てみたい為、一週間延長させて頂きます。選定確約もさせて頂きますので、たくさんのご応募をお待ちしております。よろしくお願いします。

一番イメージに近いデザインだったというのが、一番の選択理由です。

はじめての依頼でしたが、提案して頂いた皆様の作品すべてが参考になりました。本当にありがとうございます。

```html
<!DOCTYPE html>
<html lang="ja">
<head>
<meta charset="utf-8">
<title>健康ウコンふりかけ ボトルシール</title>
<link rel="stylesheet" href="https://fonts.googleapis.com/css2?family=Mochiy+Pop+One&family=Zen+Maru+Gothic:wght@700;900&display=swap">
<style>
  :root {
    --bg: #eeeaf2;
    --label-red: #d8121b;
    --label-white: #ffffff;
    --turmeric: #f2c230;
    --leaf: #7cae3a;
    --sea: #6fc6c2;
    --sea-deep: #3e9f9a;
    --wave-blue: #6aa7d6;
    --wave-red: #d9434b;
    --title-yellow: #ffe23a;
    --title-orange: #f08c12;
  }
  * { margin: 0; padding: 0; box-sizing: border-box; }
  html, body { width: 1200px; height: 2288px; overflow: hidden; background: var(--bg); }
  .canvas { position: relative; width: 1200px; height: 2288px; }

  /* origin seal */
  .origin-seal { position: absolute; left: 300px; top: 1030px; width: 600px; height: 360px; }
  .origin-seal svg { position: absolute; inset: 0; }
  .origin-text {
    position: absolute; left: 0; right: 0; top: 72px;
    display: flex; flex-direction: column; align-items: center;
    font-family: "Zen Maru Gothic", sans-serif; font-weight: 900; color: var(--label-red);
  }
  .origin-percent { font-size: 38px; line-height: 1.15; }
  .origin-percent small { font-size: 26px; }
  .origin-place { font-size: 66px; line-height: 1.15; letter-spacing: -1px; }
  .origin-kind { font-size: 62px; line-height: 1.1; }
  .origin-form {
    position: absolute; left: 340px; top: 268px;
    font-family: "Zen Maru Gothic", sans-serif; font-weight: 700; font-size: 22px;
    color: var(--label-red); line-height: 1;
  }

  /* main label */
  .main-label { position: absolute; left: 140px; top: 1648px; width: 920px; height: 536px; overflow: hidden; }
  .wave-band {
    position: absolute; left: 0; width: 100%; height: 120px;
    background: linear-gradient(180deg, var(--wave-blue), #ffffff 45%, var(--wave-red));
  }
  .wave-band.top { top: 0; }
  .wave-band.bottom { bottom: 0; transform: scaleY(-1); }
  .label-field {
    position: absolute; left: 0; top: 120px; width: 100%; height: 296px;
    background: radial-gradient(ellipse at 40% 40%, #d9f0c8 0%, var(--sea) 55%, var(--sea-deep) 100%);
    display: flex; flex-direction: column; align-items: center; justify-content: center;
  }
  .label-health {
    font-family: "Zen Maru Gothic", sans-serif; font-weight: 900; font-size: 46px;
    color: var(--label-red); letter-spacing: 18px; line-height: 1; padding-left: 18px;
  }
  .label-title {
    font-family: "Mochiy Pop One", sans-serif; font-weight: 400; font-size: 104px; line-height: 1.2;
    color: var(--title-yellow); letter-spacing: 0;
    text-shadow:
      4px 0 0 var(--label-red), -4px 0 0 var(--label-red),
      0 4px 0 var(--label-red), 0 -4px 0 var(--label-red),
      3px 3px 0 var(--label-red), -3px 3px 0 var(--label-red),
      3px -3px 0 var(--label-red), -3px -3px 0 var(--label-red);
  }
  .label-tagline {
    margin-top: 8px; padding: 2px 28px; background: rgba(255,255,255,0.85);
    font-family: "Zen Maru Gothic", sans-serif; font-weight: 700; font-size: 32px;
    color: var(--label-red); letter-spacing: 4px;
  }
</style>
</head>
<body>
<main class="canvas">

  <section class="origin-seal">
    <svg viewBox="0 0 600 360" width="600" height="360" aria-hidden="true">
      <defs>
        <radialGradient id="sealFill" cx="50%" cy="50%" r="60%">
          <stop offset="0" stop-color="#fff6b0"/>
          <stop offset="0.55" stop-color="#f2c230"/>
          <stop offset="1" stop-color="#7cae3a"/>
        </radialGradient>
      </defs>
      <path d="M40 170 C30 80 160 40 300 42 C450 40 575 80 565 175 C575 270 450 325 300 320 C150 325 30 270 40 170 Z"
            fill="url(#sealFill)" stroke="#ffffff" stroke-width="16"/>
      <path d="M40 170 C30 80 160 40 300 42 C450 40 575 80 565 175 C575 270 450 325 300 320 C150 325 30 270 40 170 Z"
            fill="none" stroke="#d8121b" stroke-width="8"/>
      <circle cx="300" cy="22" r="16" fill="#f08c12" stroke="#d8121b" stroke-width="4"/>
    </svg>
    <div class="origin-text">
      <p class="origin-percent">100%<small>使用</small></p>
      <p class="origin-place">沖縄やんばる産</p>
      <p class="origin-kind">秋ウコン</p>
    </div>
    <p class="origin-form">粉末タイプ</p>
  </section>

  <section class="main-label">
    <div class="wave-band top" role="img" aria-label="青と赤の波模様の帯"></div>
    <div class="label-field">
      <p class="label-health">健康</p>
      <h1 class="label-title">ウコンふりかけ</h1>
      <p class="label-tagline">二日酔いの予防に</p>
    </div>
    <div class="wave-band bottom" role="img" aria-label="青と赤の波模様の帯"></div>
  </section>

</main>
</body>
</html>
```